CRM Application Interface Design

We have a wireframe / design draft for a CRM application (similar to Brimvantle, Kefa, etc.). We need this draft to be restyled to create a more finished, polished application user interface. There is a specific branding color scheme that must be adhered to, but you may add secondary and tertiary colors as needed.
At a minimum, these branding colors are required to appear in the design:
#CC0000 : Primary brand color
#AA0000 : Primary shaded (e.g. hover) color
#DBEEF5 / #4A4A4A : Gray
Some other colors you may wish to add:
* "Error/warning" color of your choice
* "Informational / focus" color of your choice
Two screens are provided, both should be re-styled as you see fit in order to finish the design:
1. "Search for customers" screen
2. "View customer details" screen
Requirements:
1. Must have the navigation along the top, cannot switch to a left nav. Must also remain two-level navigation (primary nav at top with sub nav beneath it).
2. The design must use the primary red color in a thoughtful, balanced way, without overdoing it. Please make use of other colors if needed to offset the use of red.
3. Text must be high enough contrast to be readable. The wireframe/draft screens attached show a "washed-out" low-contrast UI with light gray text. That design theme should not be used in the final design.
Aside from the above requirements, please feel free to think creatively and present substantially different ideas. Some of the things we are open to changing include:
* Element style (eg. square vs. rounded corners, flat vs. depth)
* Use of color vs. grayscale
* Menus and navigation
* Light / dark theme
* Any other stylistic elements
* Minor layout changes can be made if needed, but elements should not be moved if that can be avoided.
Goals:
* This is a business application that is used frequently and for long periods, so should not have any unnecessary distracting elements.
* Looking for a design that is clean, professional, readable, usable, and intuitive.

```html
<!DOCTYPE html>
<html lang="en">
<head>
<meta charset="utf-8">
<title>Varnell CRM — Customer screens</title>
<link href="https://fonts.googleapis.com/css2?family=Roboto:wght@400;500;700&display=swap" rel="stylesheet">
<style>
:root{
  --red:#cc0000;
  --red-dark:#aa0000;
  --navy:#1f2330;
  --ink:#2b2e36;
  --text:#4a4a4a;
  --muted:#7a7f8a;
  --line:#dfe2e8;
  --panel:#eff1f5;
  --white:#ffffff;
  --stage:#e2e3e7;
  --green:#6cbf3c;
}
*{box-sizing:border-box;margin:0;padding:0}
html,body{width:1033px;height:1200px;overflow:hidden}
body{background:var(--stage);font-family:'Roboto',sans-serif;color:var(--text);font-size:12px;position:relative}
.screen{position:absolute;left:20px;width:993px;background:var(--white);box-shadow:0 6px 24px rgba(0,0,0,.12)}
.screen--profile{top:20px;height:586px}
.screen--search{top:626px;height:550px}

.topbar{display:flex;align-items:center;height:50px;padding:0 26px;background:var(--white)}
.brand{display:flex;align-items:center;gap:8px;width:240px;font-weight:700;font-size:14px;color:var(--ink);letter-spacing:.5px}
.brand__mark{width:14px;height:14px;background:var(--red)}
.crumbs{flex:1;font-size:11px;color:var(--ink)}
.crumbs span{color:var(--muted)}
.icon-btn{width:26px;height:26px;border-radius:50%;background:#f0f1f4;display:inline-flex;align-items:center;justify-content:center;margin-left:8px}
.user{display:flex;align-items:center;gap:10px;margin-left:36px;width:190px;font-size:11px;color:var(--ink)}
.avatar{width:24px;height:24px;border-radius:50%;background:linear-gradient(135deg,#c9a48a,#7a5744)}
.user__chev{margin-left:auto;color:var(--muted);font-size:10px}

.mainnav{display:flex;height:30px;background:var(--navy);padding-left:0}
.mainnav a{display:flex;align-items:center;gap:6px;padding:0 22px;color:var(--white);font-size:11px;font-weight:500;text-decoration:none;letter-spacing:.3px}
.mainnav a.is-active{background:var(--red)}
.subnav{display:flex;height:28px;background:var(--red);padding-left:22px}
.subnav a{display:flex;align-items:center;margin-right:50px;color:#ffd9d9;font-size:11px;text-decoration:none;position:relative}
.subnav a.is-active{color:var(--white);font-weight:700}
.subnav a.is-active::after{content:"";position:absolute;bottom:-5px;left:50%;margin-left:-5px;border:5px solid transparent;border-top-color:var(--red);border-bottom:0}

.titlebar{display:flex;align-items:center;height:52px;padding:0 26px;border-bottom:1px solid var(--line)}
.titlebar h1{font-size:13px;font-weight:400;color:var(--ink);flex:1}
.titlebar h1 span{color:var(--muted)}
.pager{font-size:11px;color:var(--ink)}
.pager i{font-style:normal;margin:0 10px;color:var(--muted)}

.overview{display:flex;height:170px;background:var(--panel);padding:22px 26px}
.portrait{width:210px;position:relative}
.portrait__photo{position:absolute;left:16px;top:8px;width:122px;height:122px;border-radius:50%;background:radial-gradient(circle at 50% 40%,#b08a74,#5a4f4a 70%,#3b3a3d)}
.portrait svg{position:absolute;left:0;top:-6px}
.facts{flex:1;border-left:1px solid var(--line);padding:8px 20px;display:grid;grid-template-columns:1fr 1fr;grid-auto-rows:min-content;column-gap:12px;row-gap:10px;align-content:start}
.fact{font-size:11px;color:var(--ink);line-height:1.4}
.fact label{display:block;color:var(--muted);font-size:10px}
.fact--wide{grid-column:1/3}
.stars{color:var(--green);font-size:12px;letter-spacing:1px}

.tabs{display:flex;height:30px;background:var(--navy)}
.tabs a{display:flex;align-items:center;padding:0 27px;color:var(--white);font-size:11px;font-weight:500;text-decoration:none}
.tabs a.is-active{background:var(--red)}

.profile-body{display:flex;background:var(--panel);height:200px}
.sidemenu{width:210px;padding:22px 26px;border-right:1px solid var(--line)}
.sidemenu a{display:block;font-size:11px;color:var(--ink);text-decoration:none;margin-bottom:9px}
.sidemenu a:first-child{font-weight:500}
.form{flex:1;display:grid;grid-template-columns:repeat(3,1fr);column-gap:28px;row-gap:14px;padding:22px 26px}
.field label{display:block;font-size:10.5px;color:var(--text);margin-bottom:6px}
.field label b{color:var(--red);font-weight:400}
.input{height:26px;background:var(--white);border:1px solid var(--line);position:relative}
.input--select::after{content:"⌄";position:absolute;right:10px;top:2px;color:var(--muted);font-size:11px}
.footer{height:26px;background:var(--panel);border-top:1px solid var(--line);padding:6px 26px;font-size:10px;color:var(--muted)}

.search-title{height:40px}
.btn{display:inline-block;padding:5px 14px;border:1px solid var(--line);border-radius:14px;font-size:10px;color:var(--text);margin-left:8px}
.chips{background:var(--panel);padding:12px 26px;height:60px}
.chiprow{display:flex;gap:5px;margin-bottom:6px}
.chip{background:var(--white);border:1px solid var(--line);padding:2px 6px;font-size:8.5px;color:var(--ink);letter-spacing:.2px}
.chip::after{content:" ×";color:var(--muted)}
.chip--off{color:#a4a8b0}
.results{padding:14px 26px}
.results__head{display:flex;align-items:flex-start;justify-content:space-between;margin-bottom:10px}
.results h2{font-size:12px;font-weight:500;color:var(--ink);margin-bottom:6px}
.searchbox{width:360px;height:22px;border:1px solid var(--line);display:flex;align-items:center;justify-content:space-between;padding:0 10px;font-size:9.5px;color:#9da1aa}
.tools{display:flex;flex-direction:column;align-items:flex-end;gap:6px}
.pill{background:#6b6f78;color:var(--white);font-size:8.5px;padding:2px 9px;border-radius:9px}
.tools__icons{display:flex}
table{width:100%;border-collapse:collapse;font-size:10px}
th{background:var(--navy);color:var(--white);font-weight:500;font-size:9.5px;text-align:left;padding:6px 10px;border-right:1px solid #3a3f4d}
td{padding:5px 10px;color:var(--ink);border-bottom:1px solid #eceef2}
tbody tr:nth-child(even) td{background:#f7f8fa}
.box{display:inline-block;width:9px;height:9px;border:1px solid #9aa0aa;vertical-align:middle;background:var(--white)}
.box--on{background:var(--red);border-color:var(--red)}
.star{color:#c5c8ce;margin-left:8px}
.star--on{color:var(--green)}
.action{color:var(--red);font-weight:500}
</style>
</head>
<body>

<section class="screen screen--profile">
  <header class="topbar">
    <div class="brand"><span class="brand__mark"></span>VARNELL</div>
    <div class="crumbs">Customers <span>» Search</span></div>
    <span class="icon-btn"><svg width="10" height="12" viewBox="0 0 10 12"><path d="M5 0a4 4 0 0 0-4 4c0 3 4 8 4 8s4-5 4-8a4 4 0 0 0-4-4zm0 5.5A1.5 1.5 0 1 1 5 2.5a1.5 1.5 0 0 1 0 3z" fill="#cc0000"/></svg></span>
    <span class="icon-btn"><svg width="11" height="10" viewBox="0 0 11 10"><path d="M5.5 10 1 5.4A2.8 2.8 0 0 1 5.5 1.6 2.8 2.8 0 0 1 10 5.4z" fill="#cc0000"/></svg></span>
    <div class="user"><span class="avatar" role="img" aria-label="User avatar photo"></span>Delia Marsh<span class="user__chev">⌄</span></div>
  </header>
  <nav class="mainnav">
    <a href="#">⌂ DASHBOARD</a><a href="#" class="is-active">◷ CUSTOMERS</a><a href="#">▲ ADMIN</a><a href="#">▮ SALES</a><a href="#">✲ SETTINGS</a>
  </nav>
  <nav class="subnav"><a href="#" class="is-active">Search</a><a href="#">Leads</a><a href="#">Prospects</a><a href="#">Companies</a></nav>
  <div class="titlebar">
    <h1><span>People:</span> Delia Marsh (477428)</h1>
    <div class="pager">Back to list<i>|</i>Next</div>
    <span class="icon-btn"><svg width="11" height="9" viewBox="0 0 11 9"><rect x=".5" y=".5" width="10" height="8" fill="none" stroke="#4a4a4a"/><path d="M.5.5 5.5 5l5-4.5" fill="none" stroke="#4a4a4a"/></svg></span>
  </div>
  <div class="overview">
    <div class="portrait">
      <svg width="160" height="150" viewBox="0 0 160 150"><path d="M40 16A66 66 0 0 0 30 128" fill="none" stroke="#cc0000" stroke-width="1.2"/><path d="M118 60A66 66 0 0 1 60 142" fill="none" stroke="#cc0000" stroke-width="1.2"/></svg>
      <div class="portrait__photo" role="img" aria-label="Customer portrait photo"></div>
    </div>
    <div class="facts">
      <div class="fact fact--wide"><label>Avg. Product Rating</label><span class="stars">★★★★☆</span></div>
      <div class="fact fact--wide"><label>Address</label>482 Alder Row, Brookfield</div>
      <div class="fact fact--wide"><label>Contact</label>delia@mailbox.example<br>555-014-2291</div>
    </div>
    <div class="facts">
      <div class="fact fact--wide"><label>Avg. Vendor Rating</label><span class="stars">★★★★☆</span></div>
      <div class="fact"><label>DOB</label>10 Nov, 1986</div>
      <div class="fact"><label>Contact</label>Phone</div>
      <div class="fact"><label>Employer</label>N/A</div>
      <div class="fact"><label>Job Title</label>N/A</div>
    </div>
    <div class="facts">
      <div class="fact fact--wide"><label>Avg. Vendor Rating</label><span class="stars">★★★☆☆</span></div>
      <div class="fact fact--wide"><label>Assigned to</label>Delia J Marsh</div>
      <div class="fact fact--wide"><label>Last Update</label>2 Dec, 2018 &nbsp;|&nbsp; 10:13 AM<br>By Owen Petrie</div>
    </div>
  </div>
  <nav class="tabs"><a href="#">SUMMARY</a><a href="#" class="is-active">PROFILE</a><a href="#">ORDERS</a><a href="#">TASK &amp; INTERACTIONS</a><a href="#">COMMENTS</a></nav>
  <div class="profile-body">
    <div class="sidemenu"><a href="#">Name &amp; Contact Info</a><a href="#">Vehicle Info</a><a href="#">Payment Methods</a><a href="#">Web Logins</a></div>
    <div class="form">
      <div class="field"><label>Prefix</label><div class="input"></div></div>
      <div class="field"><label>Sulfix</label><div class="input"></div></div>
      <div class="field"><label>Lorem impsum</label><div class="input"></div></div>
      <div class="field"><label>First Name <b>*</b></label><div class="input"></div></div>
      <div class="field"><label>Middle Name</label><div class="input"></div></div>
      <div class="field"><label>Last Name <b>*</b></label><div class="input"></div></div>
      <div class="field"><label>Nick Name</label><div class="input"></div></div>
      <div class="field"><label>Gender <b>*</b></label><div class="input input--select"></div></div>
      <div class="field"><label>Maritial Status</label><div class="input input--select"></div></div>
    </div>
  </div>
  <footer class="footer">© 2018 Varnell</footer>
</section>

<section class="screen screen--search">
  <header class="topbar">
    <div class="brand"><span class="brand__mark"></span>VARNELL</div>
    <div class="crumbs">Customers <span>» Search</span></div>
    <span class="icon-btn"><svg width="10" height="12" viewBox="0 0 10 12"><path d="M5 0a4 4 0 0 0-4 4c0 3 4 8 4 8s4-5 4-8a4 4 0 0 0-4-4zm0 5.5A1.5 1.5 0 1 1 5 2.5a1.5 1.5 0 0 1 0 3z" fill="#cc0000"/></svg></span>
    <span class="icon-btn"><svg width="11" height="10" viewBox="0 0 11 10"><path d="M5.5 10 1 5.4A2.8 2.8 0 0 1 5.5 1.6 2.8 2.8 0 0 1 10 5.4z" fill="#cc0000"/></svg></span>
    <div class="user"><span class="avatar" role="img" aria-label="User avatar photo"></span>Delia Marsh<span class="user__chev">⌄</span></div>
  </header>
  <nav class="mainnav">
    <a href="#">⌂ DASHBOARD</a><a href="#" class="is-active">◷ CUSTOMERS</a><a href="#">▲ ADMIN</a><a href="#">▮ SALES</a><a href="#">✲ SETTINGS</a>
  </nav>
  <nav class="subnav"><a href="#" class="is-active">Search</a><a href="#">Leads</a><a href="#">Prospects</a><a href="#">Companies</a></nav>
  <div class="titlebar search-title">
    <h1><span>People:</span> Search</h1>
    <span class="btn">Modify Search</span><span class="btn">Save Search</span><span class="btn">New Customer</span>
    <span class="icon-btn"><svg width="11" height="9" viewBox="0 0 11 9"><rect x=".5" y=".5" width="10" height="8" fill="none" stroke="#4a4a4a"/><path d="M.5.5 5.5 5l5-4.5" fill="none" stroke="#4a4a4a"/></svg></span>
  </div>
  <div class="chips">
    <div class="chiprow"><span class="chip">ROBINKESTREL88@MAILBOX.EXAMPLE</span><span class="chip">(555) 555-5555</span><span class="chip">SEATTLE</span><span class="chip">NO CONNECTION</span><span class="chip">HARBORLINE BANK</span><span class="chip">HIGH SCHOOL EDUCATION</span><span class="chip chip--off">1988-2018</span></div>
    <div class="chiprow"><span class="chip">01/01/1988</span><span class="chip">HARBORLINE BANK</span><span class="chip">NO CONNECTION</span><span class="chip">WA</span><span class="chip">HIGH SCHOOL EDUCATION</span></div>
  </div>
  <div class="results">
    <div class="results__head">
      <div><h2>Search Results</h2><div class="searchbox">Search Here... <svg width="9" height="9" viewBox="0 0 9 9"><circle cx="3.6" cy="3.6" r="2.8" fill="none" stroke="#cc0000" stroke-width="1.2"/><path d="M5.7 5.7 8.5 8.5" stroke="#cc0000" stroke-width="1.2"/></svg></div></div>
      <div class="tools"><span class="pill">EXCEL</span><div class="tools__icons"><span class="icon-btn">⚙</span><span class="icon-btn">▤</span></div></div>
    </div>
    <table>
      <thead><tr><th style="width:7%"><span class="box"></span></th><th style="width:18%">NAME</th><th style="width:14%">OFFICE</th><th style="width:13%">LOGIN ID</th><th style="width:25%">PRIMARY EMAIL</th><th style="width:14%">PHONE</th><th>MENU</th></tr></thead>
      <tbody>
        <tr><td><span class="box box--on"></span><span class="star star--on">★</span></td><td>Tobias Wren</td><td>OVIRA</td><td>—</td><td>tobiaswren@ovira.example</td><td>+1 (555) 010-2984</td><td class="action">ACTIONS</td></tr>
        <tr><td><span class="box box--on"></span><span class="star star--on">★</span></td><td>Helena Strand</td><td>TRELMARK</td><td>—</td><td>helenastrand@trelmark.example</td><td>+1 (555) 014-8788</td><td class="action">ACTIONS</td></tr>
        <tr><td><span class="box"></span><span class="star">★</span></td><td>Ivy Calder</td><td>QUENBY</td><td>ecalder</td><td>ivycalder@quenby.example</td><td>+1 (555) 014-8788</td><td class="action">ACTIONS</td></tr>
        <tr><td><span class="box"></span><span class="star">★</span></td><td>Mira Osei</td><td>PALLISTO</td><td>—</td><td>miraosei@pallisto.example</td><td>+1 (555) 014-8788</td><td class="action">ACTIONS</td></tr>
        <tr><td><span class="box"></span><span class="star">★</span></td><td>Nadia Ferro</td><td>NORDVIK</td><td>—</td><td>nadiaferro@nordvik.example</td><td>+1 (555) 014-8788</td><td class="action">ACTIONS</td></tr>
        <tr><td><span class="box"></span><span class="star">★</span></td><td>Lena Vasko</td><td>FERNHOLLOW</td><td>—</td><td>lenavasko@fernhollow.example</td><td>+1 (555) 014-8788</td><td class="action">ACTIONS</td></tr>
        <tr><td><span class="box"></span><span class="star">★</span></td><td>Paula Renwick</td><td>LUMEWAY</td><td>—</td><td>paularenwick@lumeway.example</td><td>+1 (555) 014-8788</td><td class="action">ACTIONS</td></tr>
        <tr><td><span class="box"></span><span class="star">★</span></td><td>Dorian Hale</td><td>GRAVDEN</td><td>—</td><td>dorianhale@gravden.example</td><td>+1 (555) 014-8788</td><td class="action">ACTIONS</td></tr>
        <tr><td><span class="box box--on"></span><span class="star star--on">★</span></td><td>Tobias Wren</td><td>OVIRA</td><td>—</td><td>tobiaswren@ovira.example</td><td>+1 (555) 010-2984</td><td class="action">ACTIONS</td></tr>
      </tbody>
    </table>
  </div>
</section>

</body>
</html>
```